Hydraulics Company Business Card Design

Modern business card design for a hydraulics company.
Our company colours are - black, orange and white.
I would like the following contact details included-
Name
Position
Phone number
Email
Website
Street Address

I have attached our company logo.
I would like the back of the card white.

Thank you.

```html
<!DOCTYPE html>
<html lang="en">
<head>
<meta charset="utf-8">
<title>Tarrowby Hydraulics — Business Card</title>
<link rel="stylesheet" href="https://fonts.googleapis.com/css2?family=Montserrat:wght@700&family=Roboto:wght@400&display=swap">
<style>
  :root {
    --bg: #2b2b2b;
    --black: #050505;
    --white: #ffffff;
    --orange: #f7991c;
    --rule: #bdbdbd;
    --text-light: #f2f2f2;
  }
  * { box-sizing: border-box; margin: 0; padding: 0; }
  html, body { width: 1200px; height: 880px; overflow: hidden; }
  body { background: var(--bg); position: relative; font-family: "Roboto", Arial, sans-serif; }

  .card {
    position: absolute;
    width: 620px;
    height: 355px;
    border-radius: 24px;
    overflow: hidden;
    box-shadow: 0 12px 30px rgba(0,0,0,.45);
  }

  /* Front: white with brand name */
  .card--front { left: 160px; top: 70px; background: var(--white); }
  .card--front .brand {
    position: absolute; inset: 0;
    display: flex; align-items: center; justify-content: center;
  }
  .brand-name {
    font-family: "Montserrat", Arial, sans-serif;
    font-weight: 700;
    color: var(--orange);
    line-height: 1;
    white-space: nowrap;
  }
  .card--front .brand-name { font-size: 46px; }

  /* Back: black with details */
  .card--back { left: 420px; top: 455px; background: var(--black); }
  .card--back .brand-name {
    position: absolute; right: 36px; top: 58px; font-size: 28px;
  }
  .divider {
    position: absolute; left: 40px; right: 28px; top: 168px;
    height: 1px; background: var(--rule);
  }
  .person { position: absolute; left: 40px; top: 116px; }
  .person-name {
    font-family: "Montserrat", Arial, sans-serif; font-weight: 700;
    font-size: 24px; color: var(--orange); line-height: 1;
  }
  .person-role { font-size: 16px; color: var(--text-light); margin-top: 6px; }

  .contacts { position: absolute; left: 40px; top: 186px; list-style: none; }
  .contacts li {
    display: flex; align-items: center; gap: 12px;
    font-size: 17px; color: var(--text-light); height: 27px;
  }
  .contacts svg { width: 16px; height: 16px; fill: var(--orange); flex: none; }

  .address {
    position: absolute; right: 36px; top: 186px;
    text-align: right; font-size: 16px; line-height: 1.4; color: var(--text-light);
    font-style: normal;
  }

  .band { position: absolute; bottom: 0; background: var(--orange); }
  .band--left { left: 0; width: 386px; height: 22px; }
  .band--right { right: 0; width: 226px; height: 34px; }
</style>
</head>
<body>
  <section class="card card--front" aria-label="Card front">
    <div class="brand"><span class="brand-name">Tarrowby Hydraulics</span></div>
  </section>

  <section class="card card--back" aria-label="Card back">
    <span class="brand-name">Tarrowby Hydraulics</span>

    <div class="person">
      <p class="person-name">Daniel Harper</p>
      <p class="person-role">Owner</p>
    </div>

    <div class="divider"></div>

    <ul class="contacts">
      <li>
        <svg viewBox="0 0 24 24" aria-hidden="true"><path d="M6.6 10.8a15 15 0 0 0 6.6 6.6l2.2-2.2a1 1 0 0 1 1-.25 11.4 11.4 0 0 0 3.6.57 1 1 0 0 1 1 1V20a1 1 0 0 1-1 1A17 17 0 0 1 3 4a1 1 0 0 1 1-1h3.5a1 1 0 0 1 1 1c0 1.25.2 2.45.57 3.57a1 1 0 0 1-.25 1z"/></svg>
        555.014.2290
      </li>
      <li>
        <svg viewBox="0 0 24 24" aria-hidden="true"><path d="M2 5h20v14H2z M2 5l10 8 10-8" /><path d="M3 6l9 7 9-7v-.5H3z" fill="#050505"/></svg>
        hello@tarrowbyhyd.com
      </li>
      <li>
        <svg viewBox="0 0 24 24" aria-hidden="true"><circle cx="12" cy="12" r="10"/><path d="M7 7c2 1 3 0 4 2s-2 2-1 4 3 1 3 4M15 5c-1 2 1 3 3 3M16 14c1 1 2 1 3 0" stroke="#050505" stroke-width="1.6" fill="none"/></svg>
        www.tarrowbyhyd.com
      </li>
    </ul>

    <address class="address">88 Quarry Road, Riverside<br>20417, Australia</address>

    <div class="band band--left"></div>
    <div class="band band--right"></div>
  </section>
</body>
</html>
```